Stationery for new photography studio
Flyer, Gift Certificate, Business Card, headed paper, CD label and case cover
Please note the change in email address
studio@brightferndesigns.at
Dear sir,
Thanks for your feedback.
#100 is brilliant
I really like #97. I love the colours from the photos. I like the new business cards. Could you combine the concepts in the business cards from #94 #96 #97
temp web address
http://brightferndesigns.snapvault-host.com/
#89 every thing looks great. A few comments:
1) The business cards - I like the logo side however the information side I prefer earlier designs where you used one block colour ie- #87 or #49. I'm still not sure about this side.
2) The dark black logo square on the paper looks too bold.
Great work. Thanks a lot.
Please check the newly uploaded files.
PANTONES:
Blue: 310 C
Brown: 409 C
Pink: 211 C
Gray: 424 C
FONTS:
Petra: Gotham Medium
Valkenor: Gotham Book
Tagline: Gotham Book
Signature: Custom made
I think I prefer the logo in #52 where it is slightly off the page than #70 where it is completely visible.
I like #70, it's sophisticated however the colour scheme is starting depart from the original and from the style of my work, which I think is not so heavy.
If you have any change or better suggestions please let me know.
Thank you.
#61 - #64 I'm not sure if the dots down the sides are necessary.
My website is down. But I'LL let you know when it's back up so you can take a look at some more pictures. I love the use of them in your designs. So excited by what I'm seeing. Thanks for your work so far.
#57. I love it. Everything adds up perfectly. Not sure about the font. It's a bit clumsy. I'd like something sharper and sleeker.
Great direction.
Does this work for A6
A CD disk is 120 mm in diameter (60 mm radius), with a hole 15 mm diameter (7.5 mm radius)
I'm looking on google for CD dimensions. So far I've found the case cover dimensions:
CD Cover Size Specifications for Printing
The finished dimensions for the outside of printed CD covers are 4.724 inches square. Many printed designs include bleed. The "bleed area" is an extra 1/8" of space for design elements or backgrounds to extend beyond the finished size of your piece. A CD cover with bleeds is printed slightly oversized (4.974 inches square) and then cut down to size, giving the appearance that the printing "bleeds" off the edge of the cover rather than having a white border.
Really like the direction of #51 and #52. Re. #55 I prefer the designs where all embellishments or lines are relevant. What I mean by this is that the curve does not tie in anywhere. It's an additional form that is not part of the logo.
#61 and #62 are great. Can you show me some alternative fonts for the 15% and the brightferndesigns.at
This is fun project! What size should be the CD label be? I am not too sure!
#36 with black background?
I'd be interested to see #34 with black replacing the pink.
I have uploaded information to be included in the flyers and gift certificate.
Please look at my photos to understand my style
http://www.facebook.com/BrightFern.Designs?sk=app_274930158846320

```html
<!DOCTYPE html>
<html lang="de">
<head>
<meta charset="utf-8">
<title>Petra Valkenor – Visitenkarten</title>
<link rel="stylesheet" href="https://fonts.googleapis.com/css2?family=Montserrat:wght@400;500;600&display=swap">
<style>
  :root {
    --pink: #ec8fa8;
    --pink-soft: #f4b6c6;
    --gray: #7a7674;
    --gray-dark: #5c5957;
    --ink: #111111;
    --paper: #ffffff;
    --backdrop: #e9e6e1;
    --rule: #d6d3d0;
  }
  * { box-sizing: border-box; margin: 0; padding: 0; }
  html, body { width: 1200px; height: 850px; overflow: hidden; }
  body {
    background: var(--backdrop);
    font-family: "Montserrat", sans-serif;
    position: relative;
  }
  .card {
    position: absolute;
    width: 500px;
    height: 290px;
    box-shadow: 0 6px 18px rgba(0,0,0,.18);
    overflow: hidden;
  }
  .card--info { left: 350px; top: 50px; background: var(--paper); }
  .card--white { left: 70px; top: 470px; background: var(--paper); }
  .card--black { left: 630px; top: 470px; background: var(--ink); }

  .brand {
    position: absolute;
    left: 0; right: 0;
    display: flex;
    flex-direction: column;
    align-items: center;
    gap: 10px;
  }
  .brand__mark {
    width: 34px; height: 34px;
    background: var(--pink);
  }
  .brand__name {
    font-weight: 500;
    font-size: 30px;
    letter-spacing: 3px;
    color: var(--gray);
  }
  .card--black .brand__name { color: var(--pink-soft); }
  .card--info .brand { top: 28px; }
  .card--info .brand__name { font-size: 26px; }
  .card--white .brand, .card--black .brand { top: 92px; }

  .band {
    position: absolute;
    left: 0; right: 0;
    top: 150px;
    height: 6px;
    background: var(--pink);
  }
  .details {
    position: absolute;
    left: 0; right: 0; top: 180px; bottom: 20px;
    display: flex;
    font-size: 11px;
    color: var(--gray-dark);
    line-height: 1.55;
  }
  .details__person { width: 52%; padding-left: 44px; }
  .details__person .person-name {
    color: var(--pink);
    font-weight: 600;
    font-size: 15px;
    margin-bottom: 4px;
  }
  .details__divider { width: 1px; background: var(--rule); }
  .details__contact { padding-left: 30px; padding-top: 4px; list-style: none; }
  .details__contact li { display: flex; align-items: center; gap: 7px; }
  .details__contact svg { width: 10px; height: 10px; flex: none; }
</style>
</head>
<body>
  <section class="card card--info" aria-label="Visitenkarte Rückseite">
    <div class="brand">
      <span class="brand__mark"></span>
      <span class="brand__name">Petra Valkenor</span>
    </div>
    <div class="band"></div>
    <div class="details">
      <div class="details__person">
        <p class="person-name">Petra Valkenor</p>
        <p>Lindenweg 14/3</p>
        <p>1030 Wien</p>
      </div>
      <div class="details__divider"></div>
      <ul class="details__contact">
        <li>
          <svg viewBox="0 0 10 10"><path d="M2 1h2l1 2-1.2 1a5 5 0 0 0 2.2 2.2L7 5l2 1v2c0 .6-.4 1-1 1A8 8 0 0 1 1 2c0-.6.4-1 1-1z" fill="var(--pink)"/></svg>
          06641837502
        </li>
        <li>
          <svg viewBox="0 0 10 10"><rect x="0.5" y="2" width="9" height="6.5" fill="none" stroke="var(--pink)"/><path d="M.5 2 5 5.6 9.5 2" fill="none" stroke="var(--pink)"/></svg>
          Petra@Valkenor.at
        </li>
        <li>
          <svg viewBox="0 0 10 10"><circle cx="5" cy="5" r="4.2" fill="none" stroke="var(--pink)"/><path d="M1 5h8M5 .8c2 2.4 2 6 0 8.4M5 .8c-2 2.4-2 6 0 8.4" fill="none" stroke="var(--pink)" stroke-width=".8"/></svg>
          www.BrightFernDesigns.at
        </li>
      </ul>
    </div>
  </section>

  <section class="card card--white" aria-label="Visitenkarte Vorderseite hell">
    <div class="brand">
      <span class="brand__mark"></span>
      <span class="brand__name">Petra Valkenor</span>
    </div>
  </section>

  <section class="card card--black" aria-label="Visitenkarte Vorderseite dunkel">
    <div class="brand">
      <span class="brand__mark"></span>
      <span class="brand__name">Petra Valkenor</span>
    </div>
  </section>
</body>
</html>
```